Brevant Business Card

I have a business that is called "Brevant Electrical Products LTD" My company deals with top of the range laptops and mobile phones that are exclusive. I need a business card that will be eye catching but not over complicated.

Target Market(s)

Adults aged 19 to 50
Upper middle class

Industry/Entity Type

Business

Requirements
Must have
• Company name/logo (file attached)
• It must have my contact information which is:

• Name: Dale Marwick

• Position: Managing Director 

• Business Address: 7 Hapton Row, London, W4 9QD

• Contact Number: 02085193604
• Mobile: 07814260537
• Email: info@brevant-goods.co.uk
Nice to have
• Simple and stylish
• Eye catching

```html
<!DOCTYPE html>
<html lang="en">
<head>
<meta charset="utf-8">
<title>Brevant Business Card Options</title>
<link rel="stylesheet" href="https://fonts.googleapis.com/css2?family=Arimo&family=Questrial&family=Tenor+Sans&display=swap">
<style>
  :root {
    --paper: #ffffff;
    --ink: #231f20;
    --rule: #3a3a3a;
    --brand-blue: #0090da;
    --brand-deep: #00506f;
    --sky-light: #5bb6ec;
    --emboss: #dcdcdc;
    --sheet-edge: #b5b5b5;
  }
  * { box-sizing: border-box; margin: 0; padding: 0; }
  html, body { width: 855px; height: 1200px; overflow: hidden; background: var(--paper); }
  .sheet {
    position: relative; width: 855px; height: 1200px;
    border: 1px solid var(--sheet-edge); background: var(--paper);
  }
  .section-title {
    position: absolute; left: 0; width: 855px; text-align: center;
    font-family: "Arimo", Arial, sans-serif; font-size: 33px; font-weight: 400; color: var(--ink);
  }
  .section-title.stamping { top: 68px; left: -20px; }
  .section-title.embossing { top: 650px; left: 10px; }

  .card {
    position: absolute; width: 388px; height: 237px;
    border: 1px solid var(--rule); background: var(--paper); overflow: hidden;
  }
  .col-left { left: 28px; }
  .col-right { left: 427px; }
  .row-one { top: 115px; }
  .row-two { top: 368px; }

  .panel {
    position: absolute; width: 388px; height: 238px;
    border: 1px solid var(--rule); background: var(--paper); overflow: hidden;
  }
  .panel.upper { top: 690px; }
  .panel.lower { top: 927px; }

  .front-light { background: linear-gradient(to bottom, #ffffff 0%, #f6fafd 68%, #cde7f8 82%, var(--sky-light) 100%); }
  .blue-block {
    position: absolute; left: 0; top: 0; width: 100%; height: 191px;
    background: linear-gradient(to bottom, var(--brand-blue) 0%, var(--brand-blue) 55%, #0070a6 78%, var(--brand-deep) 100%);
  }

  .wordmark {
    position: absolute; font-family: "Questrial", sans-serif;
    font-size: 78px; line-height: 1; letter-spacing: 1px; white-space: nowrap;
  }
  .wordmark.blue { color: var(--brand-blue); }
  .wordmark.white { color: #ffffff; }
  .wordmark.pale { color: var(--emboss); }
  .tagline {
    position: absolute; left: 50px; font-family: "Questrial", sans-serif;
    font-size: 28px; letter-spacing: 3.2px; color: var(--ink); white-space: nowrap; line-height: 1;
  }

  .person-name, .person-role, .contact-lines {
    position: absolute; font-family: "Tenor Sans", sans-serif; color: var(--ink); white-space: nowrap;
  }
  .person-name { font-size: 19px; line-height: 1; }
  .person-role { font-size: 15px; line-height: 1; }
  .contact-lines { font-size: 11.4px; line-height: 16px; }
  .contact-lines.large { font-size: 13.6px; line-height: 17px; }
  .contact-lines.folded { font-size: 14px; line-height: 18px; }
  .align-right { text-align: right; }

  .accent-rule { position: absolute; background: var(--brand-blue); }
</style>
</head>
<body>
<div class="sheet">

  <h1 class="section-title stamping">STAMPING: Two sides</h1>

  <!-- Option 1: light gradient front -->
  <div class="card col-left row-one front-light">
    <div class="wordmark blue" style="left:50px; top:88px;">Brevant</div>
    <div class="tagline" style="top:168px;">Electrical Products</div>
  </div>
  <div class="card col-right row-one">
    <div class="person-name" style="left:16px; top:25px;">Dale Marwick</div>
    <div class="person-role" style="left:16px; top:49px;">Managing Director</div>
    <div class="accent-rule" style="left:156px; top:25px; width:2px; height:190px;"></div>
    <div class="contact-lines" style="left:167px; top:151px;">
      Phone: 02085193604<br>
      Mobile: 07814260537<br>
      Email: info@brevant-goods.co.uk<br>
      7 Hapton Row, London, W4 9QD UK
    </div>
  </div>

  <!-- Option 2: blue block front -->
  <div class="card col-left row-two">
    <div class="blue-block"></div>
    <div class="wordmark white" style="left:52px; top:106px;">Brevant</div>
    <div class="tagline" style="top:198px;">Electrical Products</div>
  </div>
  <div class="card col-right row-two">
    <div class="person-name" style="left:19px; top:23px;">Dale Marwick</div>
    <div class="person-role" style="left:19px; top:47px;">Managing Director</div>
    <div class="accent-rule" style="left:19px; top:73px; width:346px; height:2px;"></div>
    <div class="contact-lines large align-right" style="right:22px; top:138px;">
      Phone: 02085193604<br>
      Mobile: 07814260537<br>
      Email: info@brevant-goods.co.uk<br>
      7 Hapton Row, London, W4 9QD UK
    </div>
  </div>

  <h1 class="section-title embossing">EMBOSSING: Folded card</h1>

  <!-- Folded card -->
  <div class="panel upper col-left"></div>
  <div class="panel upper col-right">
    <div class="wordmark pale" style="left:58px; top:57px;">Brevant</div>
  </div>
  <div class="panel lower col-left">
    <div class="wordmark pale" style="left:52px; top:105px;">Brevant</div>
    <div class="tagline" style="top:186px;">Electrical Products</div>
  </div>
  <div class="panel lower col-right">
    <div class="contact-lines folded" style="left:25px; top:26px;">
      Phone: 02085193604<br>
      Mobile: 07814260537<br>
      Email: info@brevant-goods.co.uk<br>
      7 Hapton Row, London, W4 9QD UK
    </div>
    <div class="person-name align-right" style="right:28px; top:163px;">Dale Marwick</div>
    <div class="person-role align-right" style="right:28px; top:188px;">Managing Director</div>
    <div class="accent-rule" style="left:232px; top:207px; width:127px; height:2px;"></div>
  </div>

</div>
</body>
</html>
```